redesign my website coralhopvoyages.net and make it user friendly

I already have a website, coralhopvoyages.net, and want a redesign in WordPress with Elementor Pro, using the same text/content. The goal is to improve:

Design quality (colors, fonts, spacing, visual flow)
User experience (easy navigation, clear offers)
Conversion readiness (calls-to-action, trust signals, booking flow)
Technical side (SEO basics, fast speed, full mobile responsiveness)

The site should look modern, clean, fun, engaging, interactive and optimized for speed and usability.

I would like the 11 page to be consolidate dto 6 as follows: Home (main landing, highlights)

Sailboat Trips (all packages, itineraries, pricing)
Boats (fleet details, features, photos)
How It Works (booking process, FAQs, travel info, what to expect)
Blog
Contact Us (form, ChatLine, phone, etc.)

Target Market(s)

sailboat trip customers for San Blas Islands in Panama

Industry/Entity Type

Travel, Boat Tour Agency

Coding

Coded - Design and coding required

Number of Pages Required

3 page

Font styles to use
Sans Serif
Other font styles liked:
• Oswalg and sans serif

Colors
0054AA
0677BA
7BADD7
CADEEF
E8F1F8
0094D4
00A9DD
6FCCEA
C7EBF8
E9F6FB
FFC000
F8CF3A
FAE287
FDF2CF
FEFAEE
F0912C
F2A743
F7CA91
FBE8D2
FDF5EE

Requirements
Must have
• Home (main landing, highlights) Sailboat Trips (all packages, itineraries, pricing) Boats (fleet details, features, photos) How It Works (booking process, FAQs, travel info, what to expect) Blog (updates, travel tips, inspiration) Contact Us (form, ChatLine, phone, etc.)
Nice to have
• I want it to look professionla and be very user friendy to entice people to contact me to book boat trips
Should not have
• a store

```html
<!DOCTYPE html>
<html lang="en">
<head>
<meta charset="utf-8">
<title>Coral Hop Voyages — San Blas Island Paradise</title>
<link href="https://fonts.googleapis.com/css2?family=Oswald:wght@500;600;700&family=Space+Grotesk:wght@400;500;600;700&display=swap" rel="stylesheet">
<style>
:root{
  --navy:#0054AA;
  --blue:#0677BA;
  --sky:#7BADD7;
  --mist:#CADEEF;
  --ice:#E8F1F8;
  --cyan:#0094D4;
  --aqua:#00A9DD;
  --lagoon:#6FCCEA;
  --foam:#E9F6FB;
  --gold:#FFC000;
  --gold-soft:#F8CF3A;
  --gold-pale:#FDF2CF;
  --cream:#FEFAEE;
  --orange:#F0912C;
  --orange-soft:#F2A743;
  --peach:#FBE8D2;
  --shell:#FDF5EE;
  --ink:#12304f;
  --text-muted:#4d6783;
  --white:#ffffff;
  --head:'Oswald', 'Arial Narrow', sans-serif;
  --sans:'Space Grotesk', Arial, sans-serif;
}
*{box-sizing:border-box;margin:0;padding:0}
html,body{width:1200px;height:3788px;overflow:hidden}
body{background:var(--white);color:var(--ink);font-family:var(--sans);font-size:14px;line-height:1.5}
a{color:inherit;text-decoration:none}
.wrap{width:1076px;margin:0 auto;position:relative}
.accent{color:var(--orange)}
.eyebrow{font-size:11px;font-weight:700;letter-spacing:1.6px;color:var(--orange);text-transform:uppercase;display:inline-block;border-bottom:2px solid var(--gold);padding-bottom:3px}
.h2{font-family:var(--head);font-size:40px;line-height:1.15;font-weight:600;color:var(--navy)}
.btn{display:inline-flex;align-items:center;justify-content:center;font-family:var(--sans);font-weight:700;border-radius:4px}
.btn-gold{background:var(--gold);color:var(--ink);box-shadow:0 4px 14px rgba(255,192,0,.35)}
.btn-ghost{border:1.5px solid var(--blue);color:var(--blue);background:var(--white)}
.arrows{display:flex;gap:8px}
.arrows span{width:34px;height:34px;border:1.5px solid var(--sky);border-radius:4px;display:flex;align-items:center;justify-content:center;background:var(--white)}

/* hero */
.hero{height:444px;position:relative;overflow:hidden}
.hero-art{position:absolute;inset:0;background:
  radial-gradient(ellipse 50% 40% at 78% 26%,rgba(242,167,67,.55),transparent 70%),
  radial-gradient(ellipse 60% 45% at 72% 72%,rgba(0,169,221,.55),transparent 75%),
  linear-gradient(90deg,#003a78 0%,#0054AA 40%,#0677BA 70%,#0094D4 100%)}
.hero-art::after{content:"";position:absolute;inset:0;background:linear-gradient(90deg,rgba(0,40,90,.85) 0%,rgba(0,40,90,.35) 45%,transparent 70%)}
.nav{position:absolute;top:26px;left:62px;right:56px;display:flex;align-items:flex-start;z-index:2;color:var(--white)}
.brand{font-family:var(--head);font-weight:600;font-size:17px;line-height:1.1;color:var(--white)}
.brand .line2{display:block}
.nav-links{display:flex;gap:26px;margin-left:174px;margin-top:3px;font-size:13px;font-weight:500}
.nav-phone{margin-left:auto;margin-top:3px;font-size:12px;color:var(--ice)}
.hero-copy{position:absolute;left:62px;top:64px;z-index:2;width:370px;color:var(--white)}
.hero-copy .eyebrow{font-size:10px;color:var(--gold)}
.hero h1{font-family:var(--head);font-weight:700;font-size:48px;line-height:47px;margin-top:12px}
.hero h1 span{color:var(--gold)}
.hero p{font-size:15px;line-height:23.5px;color:var(--ice);margin-top:18px}
.hero-cta{display:flex;align-items:center;gap:18px;margin-top:28px}
.hero-cta .btn-gold{height:44px;padding:0 26px;font-size:12px}
.hero-cta a.more{font-size:12px;font-weight:700;color:var(--gold)}

/* stats */
.stats{height:106px;background:var(--navy);position:relative;color:var(--white)}
.stats .wrap{display:grid;grid-template-columns:repeat(4,1fr);height:100%}
.stat{text-align:center;padding-top:22px;border-right:1px solid rgba(255,255,255,.15)}
.stat:last-child{border-right:0}
.stat b{display:block;font-family:var(--head);font-weight:600;font-size:28px;color:var(--gold);line-height:1.15}
.stat small{display:block;font-size:10.5px;letter-spacing:1.4px;color:var(--mist);margin-top:9px}
.chat-fab{position:absolute;right:12px;top:29px;width:48px;height:48px;border-radius:50%;background:var(--aqua);display:flex;align-items:center;justify-content:center;box-shadow:0 4px 14px rgba(0,0,0,.3)}

/* trips */
.trips{height:930px;background:var(--foam);padding-top:92px}
.section-head{display:flex;justify-content:space-between;align-items:flex-end}
.grid{display:grid;grid-template-columns:repeat(3,1fr);gap:19px;margin-top:44px}
.trip{background:var(--white);border:1px solid var(--mist);border-radius:6px;overflow:hidden;height:600px;display:flex;flex-direction:column;box-shadow:0 6px 20px rgba(0,84,170,.08)}
.trip-photo{height:200px;position:relative}
.photo-peaks{background:linear-gradient(180deg,#0054AA 0%,#7BADD7 35%,#F7CA91 50%,#CADEEF 70%,#0677BA 100%)}
.photo-wave{background:linear-gradient(180deg,#F7CA91 0%,#F2A743 25%,#7BADD7 50%,#0677BA 75%,#0054AA 100%)}
.photo-reef{background:radial-gradient(circle at 70% 40%,#6FCCEA,transparent 55%),linear-gradient(110deg,#F8CF3A 0%,#00A9DD 45%,#0094D4 70%,#0054AA 100%)}
.tag{position:absolute;left:14px;top:14px;background:var(--gold);color:var(--ink);font-size:10px;font-weight:700;padding:3px 8px;border-radius:3px;letter-spacing:.4px}
.tag.orange{background:var(--orange);color:var(--white)}
.tag.light{background:var(--white);color:var(--navy)}
.trip-body{padding:22px 22px 24px;display:flex;flex-direction:column;flex:1}
.trip h3{font-family:var(--head);font-weight:600;font-size:23px;line-height:28px;color:var(--navy)}
.trip .sub{font-size:12px;font-style:italic;color:var(--orange);margin-top:4px;line-height:19px}
.trip .desc{font-size:12.5px;color:var(--text-muted);line-height:20px;margin-top:12px}
.meta{display:flex;flex-wrap:wrap;gap:8px 22px;margin-top:14px;font-size:11px;color:var(--ink)}
.meta span{display:flex;align-items:center;gap:6px}
.meta .full{width:100%}
.price-block{margin-top:auto}
.price{font-family:var(--head);font-weight:600;font-size:30px;color:var(--navy);line-height:1}
.per{font-size:11px;color:var(--text-muted);margin-top:6px}
.trip-actions{display:flex;gap:10px;margin-top:14px}
.trip-actions .btn{height:38px;font-size:12px;flex:1}

/* experience */
.experience{height:703px;background:var(--white);padding-top:125px}
.experience .wrap{display:flex;justify-content:space-between}
.exp-copy{width:560px}
.exp-copy .h2{margin-top:12px}
.exp-copy p{font-size:15.5px;line-height:23.5px;color:var(--text-muted);margin-top:8px;width:440px}
.features{margin-top:26px;display:flex;flex-direction:column;gap:22px}
.feature{display:flex;gap:14px}
.feature i{width:38px;height:38px;border-radius:6px;background:var(--gold-pale);border:1px solid var(--gold-soft);display:flex;align-items:center;justify-content:center;flex:none}
.feature b{font-family:var(--head);font-weight:600;font-size:16px;display:block;color:var(--navy)}
.feature small{font-size:12px;color:var(--text-muted)}
.mosaic{width:418px;height:353px;margin-top:41px;display:grid;grid-template-columns:276px 136px;grid-template-rows:1fr 1fr;gap:6px}
.mosaic div{border-radius:6px}
.mosaic .tall{grid-column:2;grid-row:1/3;background:linear-gradient(180deg,#0054AA 0%,#7BADD7 38%,#F7CA91 50%,#CADEEF 70%,#0677BA 100%)}

/* reviews */
.reviews{height:553px;background:var(--shell);padding-top:129px}
.reviews .eyebrow{display:none}
.review{margin-top:46px;background:var(--white);border-top:3px solid var(--orange);border-radius:6px;height:165px;padding:22px 25px 0 30px;position:relative;box-shadow:0 6px 20px rgba(240,145,44,.1)}
.review .q{font-family:var(--head);color:var(--orange);font-size:40px;position:absolute;left:30px;top:14px;line-height:1}
.review blockquote{font-family:var(--sans);font-style:italic;font-weight:500;font-size:18px;line-height:28px;padding-left:22px;width:1000px;color:var(--ink)}
.guest{display:flex;align-items:center;gap:13px;margin-top:14px;padding-left:56px;position:relative}
.avatar{position:absolute;left:0;top:-2px;width:36px;height:36px;border-radius:50%;background:linear-gradient(135deg,#7BADD7,#0677BA)}
.guest b{font-size:12px;font-weight:700;display:block;color:var(--navy)}
.guest small{font-size:11px;color:var(--text-muted)}
.stars{position:absolute;right:25px;bottom:34px;color:var(--gold);font-size:13px;letter-spacing:1px}

/* booking */
.booking{height:685px;background:var(--ice);padding-top:140px}
.booking .wrap{display:flex;justify-content:space-between}
.book-copy{width:390px}
.book-copy .h2{margin-top:14px}
.book-copy p{font-size:15.5px;line-height:23.5px;color:var(--text-muted);margin-top:6px}
.book-copy .direct{font-size:12px;color:var(--text-muted);margin-top:30px}
.book-copy .phone{font-size:13px;font-weight:700;color:var(--navy);margin-top:6px}
.book-side{width:627px}
.form{background:var(--white);border:1px solid var(--mist);border-radius:6px;padding:26px 25px 25px;height:339px;box-shadow:0 6px 20px rgba(0,84,170,.08)}
.form label{display:block;font-size:12px;font-weight:700;margin-bottom:10px;color:var(--navy)}
.field{height:36px;border:1px solid var(--mist);background:var(--foam);border-radius:4px;display:flex;align-items:center;justify-content:space-between;padding:0 14px;font-size:12px;margin-bottom:24px;color:var(--ink)}
.form .btn-gold{width:100%;height:44px;font-size:13px;box-shadow:none}
.chat-btn{margin-top:22px;height:43px;background:var(--aqua);color:var(--white);border-radius:4px;display:flex;align-items:center;justify-content:center;gap:8px;font-size:13px;font-weight:700}

/* footer */
.footer{height:367px;background:var(--navy);padding-top:110px;color:var(--white)}
.footer-top{display:flex;height:150px}
.footer-brand{width:448px}
.footer-brand .brand .line2{color:var(--gold)}
.footer-brand small{display:block;font-size:12px;color:var(--mist);margin-top:8px}
.fcol{width:218px}
.fcol h4{font-family:var(--head);font-weight:600;font-size:15px;margin-bottom:10px;color:var(--gold)}
.fcol a{display:block;font-size:12px;color:var(--mist);line-height:25px}
.footer-bottom{border-top:1px solid rgba(255,255,255,.18);display:flex;justify-content:space-between;padding-top:16px;font-size:10.5px;color:var(--mist)}
.footer-bottom nav{display:flex;gap:20px;color:var(--white);letter-spacing:.5px;font-weight:600}
</style>
</head>
<body>

<header class="hero">
  <div class="hero-art" role="img" aria-label="Ocean wave rolling under a warm sunset sky"></div>
  <nav class="nav">
    <a class="brand" href="#">Coral Hop<span class="line2">Voyages</span></a>
    <div class="nav-links"><a href="#">Adventures</a><a href="#">Experience</a><a href="#">Reviews</a><a href="#">Booking</a></div>
    <div class="nav-phone">+507 6555 0142</div>
  </nav>
  <div class="hero-copy">
    <span class="eyebrow">Luxury Caribbean Experience</span>
    <h1>San Blas<br>Island<br><span>Paradise</span></h1>
    <p>Premium sailing adventures through pristine islands, crystal-clear waters. Experience the untouched beauty of Panama's San Blas archipelago.</p>
    <div class="hero-cta">
      <a class="btn btn-gold" href="#">Book Your Adventure</a>
      <a class="more" href="#">Learn More →</a>
    </div>
  </div>
</header>

<section class="stats">
  <div class="wrap">
    <div class="stat"><b>365</b><small>PRISTINE ISLANDS</small></div>
    <div class="stat"><b>5★</b><small>RATED EXPERIENCE</small></div>
    <div class="stat"><b>500+</b><small>HAPPY TRAVELERS</small></div>
    <div class="stat"><b>100%</b><small>PURE ADVENTURE</small></div>
  </div>
  <a class="chat-fab" href="#" aria-label="Chat with us">
    <svg width="22" height="22" viewBox="0 0 24 24" fill="none" stroke="#fff" stroke-width="2" stroke-linejoin="round"><path d="M4 5h16v11H10l-5 4v-4H4z"/></svg>
  </a>
</section>

<section class="trips">
  <div class="wrap">
    <div class="section-head">
      <h2 class="h2"><span class="accent">Luxury Sailing</span><br>Experiences</h2>
      <div class="arrows">
        <span><svg width="14" height="14" viewBox="0 0 24 24" fill="none" stroke="#0054AA" stroke-width="2"><path d="M19 12H5M11 6l-6 6 6 6"/></svg></span>
        <span><svg width="14" height="14" viewBox="0 0 24 24" fill="none" stroke="#0054AA" stroke-width="2"><path d="M5 12h14M13 6l6 6-6 6"/></svg></span>
      </div>
    </div>

    <div class="grid">
      <article class="trip">
        <div class="trip-photo photo-peaks" role="img" aria-label="Mountain peaks above a sea of clouds at dusk"><span class="tag">MOST POPULAR</span></div>
        <div class="trip-body">
          <h3>3-Day Island Adventure</h3>
          <p class="sub">Perfect introduction to San Blas paradise</p>
          <p class="desc">Perfect introduction to San Blas paradise with 5 pristine islands, crystal-clear snorkeling, and authentic Guna cultural experiences.</p>
          <div class="meta">
            <span><svg width="13" height="13" viewBox="0 0 24 24" fill="none" stroke="#F0912C" stroke-width="2"><circle cx="12" cy="12" r="9"/></svg>5 Islands</span>
            <span><svg width="13" height="13" viewBox="0 0 24 24" fill="none" stroke="#F0912C" stroke-width="2"><circle cx="12" cy="12" r="9"/><path d="M12 7v5l3 2"/></svg>3 Days</span>
            <span class="full"><svg width="13" height="13" viewBox="0 0 24 24" fill="none" stroke="#F0912C" stroke-width="2"><circle cx="12" cy="8" r="4"/><path d="M4 21c0-4 4-6 8-6s8 2 8 6"/></svg>Max 8 Guests</span>
          </div>
          <div class="price-block">
            <div class="price">$299</div><div class="per">per person</div>
            <div class="trip-actions"><a class="btn btn-gold" href="#">Book Now</a><a class="btn btn-ghost" href="#">View Details</a></div>
          </div>
        </div>
      </article>

      <article class="trip">
        <div class="trip-photo photo-wave" role="img" aria-label="Curling ocean wave under a pink evening sky"><span class="tag orange">EXTENDED JOURNEY</span></div>
        <div class="trip-body">
          <h3>5-Day Explorer</h3>
          <p class="sub">Extended journey through remote islands</p>
          <p class="desc">Venture deeper into remote islands with cultural immersion, hidden gems, and comprehensive sailing experiences for true adventurers.</p>
          <div class="meta">
            <span><svg width="13" height="13" viewBox="0 0 24 24" fill="none" stroke="#F0912C" stroke-width="2"><circle cx="12" cy="12" r="9"/></svg>10+ Islands</span>
            <span><svg width="13" height="13" viewBox="0 0 24 24" fill="none" stroke="#F0912C" stroke-width="2"><circle cx="12" cy="12" r="9"/><path d="M12 7v5l3 2"/></svg>5 Days</span>
            <span class="full"><svg width="13" height="13" viewBox="0 0 24 24" fill="none" stroke="#F0912C" stroke-width="2"><circle cx="12" cy="8" r="4"/><path d="M4 21c0-4 4-6 8-6s8 2 8 6"/></svg>Max 6 Guests</span>
          </div>
          <div class="price-block">
            <div class="price">$599</div><div class="per">per person</div>
            <div class="trip-actions"><a class="btn btn-gold" href="#">Book Now</a><a class="btn btn-ghost" href="#">View Details</a></div>
          </div>
        </div>
      </article>

      <article class="trip">
        <div class="trip-photo photo-reef" role="img" aria-label="Diver swimming beside a school of yellow fish in blue water"><span class="tag light">PREMIUM</span></div>
        <div class="trip-body">
          <h3>Private Charter</h3>
          <p class="sub">Ultimate luxury experience</p>
          <p class="desc">Your exclusive sailboat with dedicated crew, completely customized itinerary, and access to the most beautiful hidden locations.</p>
          <div class="meta">
            <span><svg width="13" height="13" viewBox="0 0 24 24" fill="none" stroke="#F0912C" stroke-width="2"><circle cx="12" cy="12" r="9"/></svg>Unlimited</span>
            <span><svg width="13" height="13" viewBox="0 0 24 24" fill="none" stroke="#F0912C" stroke-width="2"><circle cx="12" cy="12" r="9"/><path d="M12 7v5l3 2"/></svg>Flexible</span>
            <span class="full"><svg width="13" height="13" viewBox="0 0 24 24" fill="none" stroke="#F0912C" stroke-width="2"><circle cx="12" cy="8" r="4"/><path d="M4 21c0-4 4-6 8-6s8 2 8 6"/></svg>Up to 12</span>
          </div>
          <div class="price-block">
            <div class="price">$1,999</div><div class="per">per day</div>
            <div class="trip-actions"><a class="btn btn-gold" href="#">Book Now</a><a class="btn btn-ghost" href="#">View Details</a></div>
          </div>
        </div>
      </article>
    </div>
  </div>
</section>

<section class="experience">
  <div class="wrap">
    <div class="exp-copy">
      <span class="eyebrow">The Experience</span>
      <h2 class="h2"><span class="accent">Caribbean Paradise</span><br>Awaits You</h2>
      <p>Sail through crystal-clear turquoise waters to pristine white-sand beaches and vibrant coral reefs. Our professional crew delivers an unforgettable luxury experience in one of the world's most beautiful archipelagos.</p>
      <div class="features">
        <div class="feature"><i><svg width="16" height="16" viewBox="0 0 24 24" fill="none" stroke="#F0912C" stroke-width="2"><path d="M12 3l8 5-8 5-8-5z"/><path d="M4 13l8 5 8-5"/></svg></i><div><b>Luxury Sailboats</b><small>Premium vessels with comfortable cabins, spacious decks, and modern amenities.</small></div></div>
        <div class="feature"><i><svg width="16" height="16" viewBox="0 0 24 24" fill="none" stroke="#F0912C" stroke-width="2"><circle cx="12" cy="12" r="8"/><circle cx="12" cy="12" r="3"/></svg></i><div><b>Professional Crew</b><small>Expert captains, chefs and guides with intimate knowledge of San Blas.</small></div></div>
        <div class="feature"><i><svg width="16" height="16" viewBox="0 0 24 24" fill="none" stroke="#F0912C" stroke-width="2"><rect x="6" y="4" width="12" height="16" rx="1"/><path d="M9 9h6M9 13h6"/></svg></i><div><b>All-Inclusive</b><small>Gourmet meals, premium drinks, activities and equipment included.</small></div></div>
      </div>
    </div>
    <div class="mosaic">
      <div class="photo-reef" role="img" aria-label="Diver among a school of yellow reef fish"></div>
      <div class="tall" role="img" aria-label="Mountain summit above clouds at twilight"></div>
      <div class="photo-wave" role="img" aria-label="Ocean wave at sunset"></div>
    </div>
  </div>
</section>

<section class="reviews">
  <div class="wrap">
    <div class="section-head">
      <h2 class="h2"><span class="accent">Words From</span><br>Our Guests</h2>
      <div class="arrows">
        <span><svg width="14" height="14" viewBox="0 0 24 24" fill="none" stroke="#0054AA" stroke-width="2"><path d="M19 12H5M11 6l-6 6 6 6"/></svg></span>
        <span><svg width="14" height="14" viewBox="0 0 24 24" fill="none" stroke="#0054AA" stroke-width="2"><path d="M5 12h14M13 6l6 6-6 6"/></svg></span>
      </div>
    </div>
    <div class="review">
      <span class="q">"</span>
      <blockquote>"Perfect organization from start to finish. Captain knew all the best spots, food was amazing, and the cultural experience was authentic. This is paradise found!"</blockquote>
      <div class="guest"><span class="avatar" role="img" aria-label="Guest portrait"></span><div><b>Lukas Brandt</b><small>Berlin, Germany</small></div></div>
      <div class="stars">★★★★★</div>
    </div>
  </div>
</section>

<section class="booking">
  <div class="wrap">
    <div class="book-copy">
      <span class="eyebrow">Book Your Adventure</span>
      <h2 class="h2"><span class="accent">Ready to Discover</span><br>Paradise?</h2>
      <p>Book your luxury sailing adventure now and experience the magic of San Blas. Limited spots available for our premium adventures.</p>
      <div class="direct">Or contact us directly:</div>
      <div class="phone">+507 6555 0142</div>
    </div>
    <div class="book-side">
      <form class="form">
        <label>Adventure</label>
        <div class="field">Select Adventure <span>⌄</span></div>
        <label>Date</label>
        <div class="field">mm/dd/yyyy <span style="color:#7BADD7">▭</span></div>
        <label>Guests</label>
        <div class="field">Select Guests <span>⌄</span></div>
        <a class="btn btn-gold" href="#">Check Availability</a>
      </form>
      <a class="chat-btn" href="#"><svg width="16" height="16" viewBox="0 0 24 24" fill="none" stroke="#fff" stroke-width="2" stroke-linejoin="round"><path d="M4 5h16v11H10l-5 4v-4H4z"/></svg>Quick Quote via ChatLine</a>
    </div>
  </div>
</section>

<footer class="footer">
  <div class="wrap">
    <div class="footer-top">
      <div class="footer-brand"><div class="brand">Coral Hop<span class="line2">Voyages</span></div><small>Premium Caribbean Sailing Adventures</small></div>
      <div class="fcol"><h4>Adventures</h4><a href="#">3-Day Adventure</a><a href="#">5-Day Explorer</a><a href="#">Private Charter</a></div>
      <div class="fcol"><h4>Company</h4><a href="#">About Us</a><a href="#">Our Fleet</a><a href="#">Contact</a></div>
      <div class="fcol"><h4>Contact</h4><a href="#">+507 6555 0142</a><a href="#">info@coralhopvoyages.net</a><a href="#">Panama City, Panama</a></div>
    </div>
    <div class="footer-bottom">
      <span>© 2025 Coral Hop Voyages. All rights reserved.</span>
      <nav><a href="#">PHOTO FEED</a><a href="#">COMMUNITY</a><a href="#">REVIEW HUB</a></nav>
    </div>
  </div>
</footer>

</body>
</html>
```